Growing Wellness Company Needs an Amazing Cover for a series of Booklets

We are publishing our own series of booklets on health & wellness topics, called Vital Spark Primers and need an inspiring, modern design for the cover. We are beginning with the Title Diabetes: Type 2, but we will use this design for other titles later one.

SIZE:
This will be the front and back of a 8.5 x 5.5 booklet, plus 2 sample interior pages.

COLOR:
We are an industry leaders and prefer touse vibrant colors and designs to inspire our clients to change to a healthier lifestyle.

REQUIREMENTS:
I am attaching our Vital Spark logo, which needs to be on each cover, but does not need to be the focal point. You may you the words vital spark or just the b logo. The topic/title needs to be no lower than 1/2" from the top of the cover.

I'm attaching some samples of items I like, but please be creative!
If you would like to see some of our other in-house samples of publications send me a message and I'll show you. I will give detailed feedback so dive in and get creative!
Updates

FRONT COVER: 
1. Can you please make sure the title is in the top 1.5" of the page, i can't tell from this view. 
Type 2 Diabetes (1st line, bigger) 
A Simple Guide to Understanding & Controlling Your Blood Sugar (Second Row, much smaller) this can also be below the 1.5" line if it needs to be. 
3.We would like to see three shapes maybe toward the bottom with these words in them, one word per shape. inspire, equip, succeed 

IMAGE 
1. We would like you to leave a placeholder for an image, but would like to see different shapes, such as a rounded square or rectangle or a rectangle with two square corners and two rounded corners. 
2. Please play with some different border options as well,

BACKSIDE 
1. please put our information on the back side on the bottom, small. the information i will put in a file on the brief, the 2nd page has our address, phone, etc. 
2. Add our MC logo (attached as an image in the design brief)

Thanks! looking forward to what else you have. 

Reason: I want to give more time to get more/better designs in, i know this is a little more involved project.

Reason: Still not happy with designs, would like to see more.

Hello - thank you for submitting designs, the designs are getting a little too busy....here is a website I love the simplicity of...thanks!  http://www.brindlevalecare.example   

Reason: We are getting closer to narrowing it down, I want to give the designers a few more days to tweak their designs, then i will ask the final 2 or 3 to submit a couple version of the inside pages. I will supply text for those so you know what you're working with. Thanks!

Target Market(s)

Our clients are adults, about 50/50 men & women in the age range from 20-70 with most being in their early 50's. from high school education up to professional degrees

Industry/Entity Type

Industry

Font styles to use
Serif
Sans Serif
Script

Colors
a64599
e34197
00a98f
9bcb3c
ffc214
f78f20
f37122
0492cd
6a439a

Requirements
Must have
• Eye catching, inspiring design that entices people to read our booklet:

I need a front and back cover and 2 interior page samples , we will be using more of an info graphic style inside possible with a few actual photographs

FRONT COVER REQUIREMENTS:
Title (must be no lower than 1.5" below the top)
Vital Spark Logo (attached in pink and green)
Meadowcrest Wellness' Logo

BACK COVER REQUIREMENTS:
a place for summary text
meadowcrest wellness contact information
a place for an item # (can be small, no barcode)
Nice to have
• the colors i chose are samples, does not need to include every color, each title we write will have a different color story

I can appreciate a white cover with some amazing art of pops of color, but i would also love a really rich color with subtle tone on tone things (see the navy blue cover picture)
Should not have
• boring colors, lots of pictures, typical booklet design

```html
<!DOCTYPE html>
<html lang="en">
<head>
<meta charset="utf-8">
<title>Vital Spark Primers – Diabetes 2 Booklet</title>
<link rel="stylesheet" href="https://fonts.googleapis.com/css2?family=Open+Sans:wdth,wght@75..100,300..800&display=swap">
<style>
  :root{
    --stage:#e6e6e6;
    --plum:#6a1b7c;
    --plum-deep:#4c0f5b;
    --plum-light:#8a2d96;
    --teal:#00a98f;
    --lime:#9bcb3c;
    --sun:#ffc214;
    --orange:#f37122;
    --sky:#0492cd;
    --white:#ffffff;
    --soft:#e9d6ee;
  }
  *{box-sizing:border-box;margin:0;padding:0}
  html,body{width:1200px;height:786px;overflow:hidden;background:var(--stage)}
  body{position:relative;font-family:"Open Sans",Arial,sans-serif;color:var(--white)}
  .panel{position:absolute;top:133px;width:520px;height:520px;overflow:hidden;
    background:linear-gradient(160deg,var(--plum-light) 0%,var(--plum) 45%,var(--plum-deep) 100%)}
  .panel--back{left:80px}
  .panel--front{left:600px;border-left:1px solid rgba(255,255,255,.12)}
  .panel svg.shapes{position:absolute;inset:0}
  .abs{position:absolute}
  .title{font-weight:800;font-stretch:75%;letter-spacing:-1px;line-height:1;text-transform:uppercase}
  .kicker{font-weight:300;text-transform:uppercase;letter-spacing:.5px}
  .small{font-size:8.5px;line-height:1.45}
  .center{text-align:center}

  /* back */
  .back-title{left:60px;top:52px;font-size:56px}
  .back-sub{left:64px;top:112px;font-size:12px}
  .symptoms{left:34px;top:180px;width:124px}
  .symptoms h3{font-size:11px;font-weight:700;margin-bottom:5px;text-align:center;white-space:nowrap}
  .symptoms ul{list-style:none;padding-left:6px}
  .symptoms li{font-size:8.5px;line-height:1.6;padding-left:10px;position:relative}
  .symptoms li::before{content:"";position:absolute;left:0;top:4px;width:5px;height:5px;background:var(--white);border-radius:1px}
  .stat{left:56px;top:312px;width:80px}
  .stat .small{font-size:7.5px;line-height:1.3}
  .stat .figure{font-size:30px;font-weight:800;font-stretch:75%;line-height:1}
  .lifestyle{left:172px;top:305px;width:88px;font-weight:700;font-size:12px;line-height:1.15}
  .lifestyle .amp{display:block;font-size:28px;font-weight:800;line-height:1.1}
  .cause{left:282px;top:232px;width:140px}
  .cause h3{font-size:15px;font-weight:700;text-align:center;margin-bottom:6px}
  .prevent{left:228px;top:428px;width:94px;font-size:14px;font-weight:800;font-stretch:75%;line-height:1.05;text-transform:uppercase}

  /* front */
  .front-kicker{left:110px;top:88px;font-size:16px}
  .front-title{left:104px;top:110px;font-size:66px}
  .what{left:262px;top:206px;font-size:13px;font-weight:300;text-transform:uppercase}
  .what b{font-weight:800}
  .intro{left:262px;top:232px;width:220px}
  .intro p{margin-bottom:8px;color:var(--soft)}

  .brand{right:26px;bottom:22px;display:flex;align-items:center;gap:6px;font-size:12px;font-weight:700;color:var(--lime)}
  .brand .dot{width:12px;height:12px;border-radius:50%;background:var(--lime)}
</style>
</head>
<body>

<!-- Back cover -->
<section class="panel panel--back">
  <svg class="shapes" width="520" height="520" viewBox="0 0 520 520" aria-hidden="true">
    <g fill="none" stroke="#ffffff" stroke-opacity=".06" stroke-width="1.2">
      <path d="M0 380 C120 300 260 470 520 340"/>
      <path d="M0 410 C140 330 280 500 520 370"/>
      <path d="M0 440 C150 360 300 520 520 400"/>
    </g>
    <circle cx="190" cy="295" r="150" fill="var(--plum-deep)"/>
    <circle cx="350" cy="320" r="112" fill="var(--lime)"/>
    <circle cx="96" cy="232" r="76" fill="var(--teal)"/>
    <circle cx="96" cy="345" r="52" fill="var(--sky)"/>
    <circle cx="216" cy="338" r="58" fill="var(--orange)"/>
    <circle cx="275" cy="448" r="50" fill="var(--sun)"/>
  </svg>

  <h1 class="abs title back-title">Diabetes 2</h1>
  <p class="abs kicker back-sub">Information &amp; Summary</p>

  <div class="abs symptoms">
    <h3>Signs &amp; Symptoms</h3>
    <ul>
      <li>Frequent thirst</li>
      <li>Tired most days</li>
      <li>Blurred vision</li>
      <li>Slow healing cuts</li>
    </ul>
  </div>

  <div class="abs stat center">
    <p class="small">Preventable in up to</p>
    <p class="figure">90%</p>
    <p class="small">of cases</p>
  </div>

  <div class="abs lifestyle center">Improve your lifestyle <span class="amp">&amp;</span></div>

  <div class="abs cause">
    <h3>Cause</h3>
    <p class="small center">Type 2 diabetes develops when the body stops using insulin well. Extra weight, little activity, family history and age all raise the risk. Over time, sugar builds up in the blood and can harm the heart, eyes, nerves and kidneys.</p>
  </div>

  <div class="abs prevent center">Prevent<br>Diabetes</div>

  <div class="abs brand"><span class="dot"></span>Vital Spark</div>
</section>

<!-- Front cover -->
<section class="panel panel--front">
  <svg class="shapes" width="520" height="520" viewBox="0 0 520 520">
    <g fill="none" stroke="#ffffff" stroke-opacity=".06" stroke-width="1.2" aria-hidden="true">
      <path d="M0 120 C160 40 320 200 520 90"/>
      <path d="M0 420 C150 340 300 500 520 380"/>
      <path d="M0 450 C160 370 310 520 520 410"/>
    </g>
    <g aria-hidden="true">
      <ellipse cx="100" cy="300" rx="64" ry="50" fill="var(--teal)"/>
      <ellipse cx="165" cy="270" rx="56" ry="40" fill="var(--sun)"/>
      <ellipse cx="202" cy="345" rx="36" ry="60" fill="var(--sky)"/>
      <ellipse cx="70" cy="375" rx="40" ry="34" fill="var(--lime)"/>
      <ellipse cx="138" cy="398" rx="56" ry="32" fill="var(--orange)"/>
    </g>
    <defs>
      <radialGradient id="portraitTone" cx="50%" cy="40%" r="60%">
        <stop offset="0" stop-color="#d9dde2"/>
        <stop offset="1" stop-color="#8f99a6"/>
      </radialGradient>
    </defs>
    <circle cx="138" cy="332" r="72" fill="var(--white)"/>
    <circle cx="138" cy="332" r="68" fill="url(#portraitTone)" role="img" aria-label="Portrait photo of a smiling grey-haired man"/>
  </svg>

  <p class="abs kicker front-kicker">Learn how to tackle and beat</p>
  <h2 class="abs title front-title">Diabetes 2</h2>

  <p class="abs what">What is <b>diabetes?</b></p>
  <div class="abs intro small">
    <p>Diabetes is a condition where blood sugar stays too high because the body cannot use insulin properly.</p>
    <p>Type 2 is the most common form. It often grows slowly over years, and many people do not notice signs at first.</p>
    <p>The good news: small daily changes can help you manage it.</p>
  </div>

  <div class="abs brand"><span class="dot"></span>Vital Spark</div>
</section>

</body>
</html>
```